Website Voskamp detective agency

Hi all,
After my last posted job for a logo (see attached file) I now need a website for my detective agency (Recherchebureau in Dutch)
I already have the better logo then my competitors thanks to you and your colleges working with Brandforge.
Please google the word recherchebureau to see what the competition has.
I will leave it up to you.
Bare in mind I take jobs from companies (staff steeling data or products) and private people (divorce matters etc.) so it should look very professional, trustworthy and different from the others.
My company uses creativity and new/ different ways to find the truth.
I think the logo already reflects this.
Of course I need it sliced for the website builder but if you can built it too please let me know. Then I would need a template were I can upload text and photo's etc.
Target Market(s)
Corporations
Small business
Privat people
Industry/Entity Type
Detective
Coding
Coded - Design and coding required
Number of Pages Required
5+ page
Requirements
Must have
- Responsive!
- Also this logo:
- http://www.kvbwacht.nl/wp-content/uploads/2014/05/keurmerk.png
- With the line:
- Erkend door het college van toezicht en certificering
- (This means recognized by the board of oversight)
Nice to have
- Here some extra.
- It is about website trend which I think is true.
- Please use google translate because it is in Dutch.
- http://www.lumenpost.com/archive/2014/11/17/10-webdesigntrends-voor-2015/

```html
<!DOCTYPE html>
<html lang="nl">
<head>
<meta charset="utf-8">
<title>Voskamp Recherchebureau</title>
<link href="https://fonts.googleapis.com/css2?family=Open+Sans:wght@400;600;700;800&display=swap" rel="stylesheet">
<style>
  :root{
    --teal:#1f9bbd;
    --teal-box:rgba(31,140,185,.88);
    --ink:#2b3336;
    --topbar:#2c383c;
    --footer:#33403f;
    --footer-deep:#252f31;
    --muted:#9aa3a6;
    --white:#ffffff;
  }
  *{box-sizing:border-box;margin:0;padding:0}
  html,body{width:811px;height:1200px;overflow:hidden}
  body{font-family:"Open Sans",Arial,sans-serif;background:var(--white);color:var(--ink);position:relative}

  .topbar{height:28px;background:var(--topbar);color:#cfd6d8;font-size:8.5px;display:flex;align-items:center;padding:0 56px;gap:26px}
  .topbar .item{display:flex;align-items:center;gap:6px}
  .topbar .dot{width:13px;height:13px;border-radius:50%;background:var(--teal);display:flex;align-items:center;justify-content:center}

  .header{height:66px;display:flex;align-items:center;justify-content:space-between;padding:0 40px 0 56px;border-bottom:1px solid #e4e8e9}
  .brand{display:flex;align-items:center;gap:8px;color:var(--ink);text-transform:uppercase;line-height:1}
  .brand-mark{width:18px;height:18px;background:var(--ink);flex:none}
  .brand-name{display:block;font-weight:800;font-size:17px;letter-spacing:1px}
  .brand-sub{display:block;font-weight:600;font-size:8px;letter-spacing:1.6px;margin-top:3px}
  .nav{display:flex;align-self:stretch;font-size:8px;font-weight:700;text-transform:uppercase;white-space:nowrap}
  .nav a{color:var(--ink);text-decoration:none;padding:0 10px;display:flex;align-items:center}
  .nav a.active{background:var(--teal);color:var(--white)}

  .hero{position:relative;height:366px;background:linear-gradient(180deg,#7d8a93 0%,#5e6d78 45%,#3a4650 75%,#2a333b 100%)}
  .services{position:absolute;left:76px;right:67px;top:203px;display:flex;justify-content:space-between}
  .service{width:148px;height:148px;background:var(--teal-box);border:2px solid rgba(255,255,255,.55);display:flex;flex-direction:column;align-items:center;justify-content:flex-end;padding-bottom:14px;color:var(--white);font-size:10.5px;font-weight:700;text-transform:uppercase;letter-spacing:.3px}
  .service svg{margin-bottom:14px}

  .intro{text-align:center;padding:38px 120px 0}
  .intro h1{font-size:16px;font-weight:800;letter-spacing:.4px;text-transform:uppercase}
  .intro p{font-size:8px;color:var(--muted);margin-top:8px;line-height:1.6}

  .cards{display:flex;justify-content:space-between;padding:0 73px 0 68px;margin-top:44px}
  .card{width:203px;text-align:center}
  .card .photo{height:146px}
  .card h2{font-size:11px;font-weight:700;margin-top:10px}
  .card p{font-size:7.5px;color:var(--muted);line-height:1.65;margin-top:6px;padding:0 6px}

  .footer{position:absolute;top:918px;left:0;width:811px;height:238px;background:var(--footer);color:#c4cccd;display:flex;padding:24px 56px 0;gap:40px}
  .footer .col{flex:1;font-size:7.5px;line-height:1.65}
  .footer .brand{color:var(--white);margin-bottom:14px}
  .footer .brand-mark{background:var(--white)}
  .footer p+p{margin-top:8px}
  .footer ul{list-style:none}
  .footer li{margin-bottom:12px}
  .footer li strong{display:flex;align-items:center;gap:8px;color:var(--white);font-size:8px;font-weight:600}
  .footer li strong span{width:13px;height:13px;background:var(--white);display:inline-block;flex:none}
  .footer li p{margin:5px 0 0 21px}
  .badge{width:70px;height:70px;border-radius:50%;background:#dfe5e6;margin-bottom:14px}
  .bottombar{position:absolute;top:1156px;left:0;width:811px;height:44px;background:var(--footer-deep);color:#8e989a;font-size:7.5px;display:flex;align-items:center;justify-content:center}
</style>
</head>
<body>
  <div class="topbar">
    <div class="item"><span class="dot"><svg width="8" height="8" viewBox="0 0 10 10"><path d="M2 1l2 2-1 1.5c.6 1.2 1.3 1.9 2.5 2.5L7 6l2 2-1.5 1.5C4.5 9 1 5.5.5 2.5z" fill="#fff"/></svg></span>+31 (0)6 48 20 51 76</div>
    <div class="item"><span class="dot"><svg width="8" height="8" viewBox="0 0 10 10"><circle cx="5" cy="5" r="4" fill="none" stroke="#fff"/><path d="M5 2.5V5h2" stroke="#fff" fill="none"/></svg></span>Monday - Sunday 9.00 - 18.00</div>
    <div class="item"><span class="dot"><svg width="8" height="8" viewBox="0 0 10 10"><rect x="1" y="2.5" width="8" height="5" fill="none" stroke="#fff"/><path d="M1 2.5l4 3 4-3" stroke="#fff" fill="none"/></svg></span>contact@voskamp.nl</div>
  </div>

  <header class="header">
    <div class="brand"><span class="brand-mark"></span><span><span class="brand-name">Voskamp</span><span class="brand-sub">Recherchebureau</span></span></div>
    <nav class="nav">
      <a class="active">Home</a><a>Bedrijfsrecherche ▾</a><a>Prive detective ▾</a><a>Opleidingen</a><a>Laatste nieuws</a><a>Contact</a>
    </nav>
  </header>

  <section class="hero" role="img" aria-label="Photograph of canal houses along a city canal at dusk">
    <div class="services">
      <div class="service"><svg width="60" height="46" viewBox="0 0 60 46"><circle cx="22" cy="26" r="14" fill="none" stroke="#fff" stroke-width="5"/><circle cx="38" cy="26" r="14" fill="none" stroke="#fff" stroke-width="5"/></svg>Echtscheiding</div>
      <div class="service"><svg width="60" height="46" viewBox="0 0 60 46"><circle cx="24" cy="20" r="13" fill="none" stroke="#fff" stroke-width="5"/><path d="M33 30l12 12" stroke="#fff" stroke-width="6" stroke-linecap="round"/></svg>Personen zoeken</div>
      <div class="service"><svg width="60" height="46" viewBox="0 0 60 46"><circle cx="30" cy="12" r="8" fill="#fff"/><path d="M18 44l4-22h16l4 22z" fill="#fff"/></svg>Stelen zoeken</div>
      <div class="service"><svg width="60" height="46" viewBox="0 0 60 46"><path d="M20 2c0 14 20 14 20 21s-20 7-20 21M40 2c0 14-20 14-20 21s20 7 20 21" fill="none" stroke="#fff" stroke-width="4"/></svg>DNA onderzoek</div>
    </div>
  </section>

  <section class="intro">
    <h1>Toonaangevende internationale recherchebureau</h1>
    <p>We deliver discreet and thorough investigations for companies and private clients across the Netherlands and abroad, using creative methods and proven techniques to uncover the facts you need.</p>
  </section>

  <section class="cards">
    <article class="card">
      <div class="photo" role="img" aria-label="Photograph of a business meeting around a table" style="background:linear-gradient(135deg,#d9dfe2,#9ea9ae)"></div>
      <h2>Bedrijfsrecherches</h2>
      <p>Theft of data or stock by staff, internal fraud and breaches of contract are traced with care and reported in clear, usable findings.</p>
    </article>
    <article class="card">
      <div class="photo" role="img" aria-label="Photograph of a camera lens in close-up" style="background:linear-gradient(135deg,#cfd4d6,#555b5e)"></div>
      <h2>Prive detective</h2>
      <p>Divorce matters, suspected infidelity and missing persons are handled with full discretion, respect and attention to every detail of your case.</p>
    </article>
    <article class="card">
      <div class="photo" role="img" aria-label="Photograph of hands typing on a laptop keyboard" style="background:linear-gradient(135deg,#e4e7e8,#8a9295)"></div>
      <h2>Bedrijfsfraude</h2>
      <p>Financial fraud, false sick leave and insurance claims are examined by our specialists so you can act on solid, verified evidence.</p>
    </article>
  </section>

  <footer class="footer">
    <div class="col">
      <div class="brand"><span class="brand-mark"></span><span><span class="brand-name">Voskamp</span><span class="brand-sub">Recherchebureau</span></span></div>
      <p>Voskamp Recherchebureau is a licensed agency working for businesses and private clients. Every case is handled in strict confidence by experienced investigators.</p>
      <p>Creative methods and modern tools help us find the truth where others stop looking.</p>
    </div>
    <div class="col">
      <ul>
        <li><strong><span></span>Stealing onderzoek</strong><p>Staff theft of goods or data is traced quickly and quietly, with a full report for legal follow-up.</p></li>
        <li><strong><span></span>Personen zoeken</strong></li>
        <li><strong><span></span>Partner onderzoek</strong></li>
        <li><strong><span></span>DNA onderzoek</strong></li>
      </ul>
    </div>
    <div class="col">
      <div class="badge" role="img" aria-label="Certification badge"></div>
      <p>Erkend door het college van toezicht en certificering</p>
    </div>
  </footer>
  <div class="bottombar">Copyright © 2015 Voskamp Recherchebureau. All rights reserved.</div>
</body>
</html>
```